shutter business card and postcard design

Custom Interior and Exterior Shutters manufactured In Houston Texas Made in USA we offer fast delivery lifetime warranty
Dean Whitfield owner has been manufacturing shutters in houston for over 44 years
nedd to use one of the pictures provided and add company name phone number on face Louver Loft (281)555-0187
back side
louver loft
8217 calloway ln.
houston, texas 77099
email louverloft@examplemail.test
website louverlofthouston.test

Industry/Entity Type

Business

```html
<!DOCTYPE html>
<html lang="en">
<head>
<meta charset="utf-8">
<title>Louver Loft – Business Card</title>
<link href="https://fonts.googleapis.com/css2?family=Open+Sans:wght@400;600;700;800&display=swap" rel="stylesheet">
<style>
  :root {
    --backdrop: #9c9c9c;
    --gold: #e3a232;
    --gold-light: #f0c46e;
    --gold-deep: #c98a1e;
    --ink: #1b1b1b;
    --muted: #9a9a9a;
    --paper: #ffffff;
  }
  * { box-sizing: border-box; margin: 0; padding: 0; }
  html, body { width: 1200px; height: 960px; overflow: hidden; }
  body {
    background: var(--backdrop);
    font-family: "Open Sans", sans-serif;
    position: relative;
  }
  .card {
    position: absolute;
    left: 230px;
    width: 740px;
    height: 423px;
    overflow: hidden;
    box-shadow: 0 6px 18px rgba(0,0,0,.25);
  }
  .card--front { top: 36px; }
  .card--back { top: 500px; background: var(--paper); }

  /* Front */
  .front-photo {
    position: absolute; inset: 0;
    background: linear-gradient(135deg, var(--gold-light) 0%, var(--gold) 45%, var(--gold-deep) 100%);
  }
  .front-brand {
    position: absolute; left: 60px; top: 70px;
    color: var(--paper);
    font-weight: 800; font-size: 104px; line-height: 1;
    letter-spacing: -1px;
  }
  .front-tagline {
    position: absolute; left: 64px; top: 190px;
    color: var(--paper); font-weight: 600; font-size: 30px;
  }
  .front-rule {
    position: absolute; left: 200px; top: 252px;
    width: 340px; height: 2px; background: rgba(255,255,255,.85);
  }
  .front-perks {
    position: absolute; left: 64px; top: 284px;
    display: flex; align-items: center; gap: 18px;
    color: var(--paper); font-weight: 600; font-size: 27px; line-height: 1.25;
  }
  .front-usa {
    position: absolute; left: 430px; top: 330px;
    display: flex; align-items: center; gap: 16px;
    color: var(--paper); font-weight: 600; font-size: 29px;
  }

  /* Back */
  .back-header {
    position: absolute; left: 0; top: 0; width: 100%; height: 118px;
    background: linear-gradient(90deg, var(--gold) 0%, var(--gold-light) 70%, #f7e2b6 100%);
  }
  .back-brand {
    position: absolute; left: 28px; top: 16px;
    color: var(--paper); font-weight: 800; font-size: 46px; line-height: 1;
  }
  .back-tagline {
    position: absolute; left: 30px; top: 70px;
    color: var(--paper); font-weight: 600; font-size: 14px;
  }
  .back-divider {
    position: absolute; left: 452px; top: 22px; width: 1px; height: 74px;
    background: rgba(255,255,255,.8);
  }
  .back-call {
    position: absolute; left: 478px; top: 26px;
    display: flex; align-items: center; gap: 14px;
  }
  .back-call__text { color: var(--ink); line-height: 1.15; }
  .back-call__label { font-weight: 700; font-size: 24px; }
  .back-call__number { font-size: 24px; }
  .back-header-line {
    position: absolute; left: 0; top: 118px; width: 100%; height: 4px; background: var(--gold);
  }
  .back-services {
    position: absolute; left: 30px; top: 136px;
    color: var(--muted); font-size: 15px; line-height: 1.3;
  }
  .back-address {
    position: absolute; left: 30px; top: 196px;
    color: var(--ink); font-size: 21px; line-height: 1.3;
  }
  .back-address__name { font-weight: 700; }
  .back-person {
    position: absolute; right: 34px; top: 176px; text-align: right;
  }
  .back-person__name { font-weight: 700; font-size: 30px; color: var(--ink); line-height: 1.1; }
  .back-person__title { font-size: 13px; color: var(--gold); letter-spacing: 1px; }
  .back-contacts {
    position: absolute; right: 34px; top: 262px;
    font-size: 19px; color: var(--ink); line-height: 1.55; text-align: right;
  }
  .back-contacts li { list-style: none; display: flex; align-items: center; justify-content: flex-end; gap: 10px; }
  .back-footer {
    position: absolute; left: 0; bottom: 0; width: 100%; height: 42px; background: var(--ink);
  }
  .back-web {
    position: absolute; left: 0; bottom: 0; width: 360px; height: 62px;
    background: var(--gold);
    color: var(--paper); font-weight: 600; font-size: 19px;
    display: flex; align-items: center; padding-left: 30px;
  }
</style>
</head>
<body>

<section class="card card--front">
  <div class="front-photo" role="img" aria-label="Interior photo of a room with arched windows and plantation shutters, tinted gold"></div>
  <div class="front-brand">Louver Loft</div>
  <div class="front-tagline">Houston’s Source for Plantation Shutters</div>
  <div class="front-rule"></div>
  <div class="front-perks">
    <svg width="58" height="44" viewBox="0 0 58 44" aria-hidden="true">
      <g fill="none" stroke="#fff" stroke-width="3" stroke-linejoin="round">
        <path d="M16 8h26v24H16z"/>
        <path d="M42 16h8l6 8v8H42z"/>
      </g>
      <circle cx="24" cy="35" r="5" fill="#fff"/>
      <circle cx="48" cy="35" r="5" fill="#fff"/>
      <g stroke="#fff" stroke-width="3"><path d="M0 14h12M3 20h9M6 26h6"/></g>
    </svg>
    <div>Fast Delivery<br>Lifetime Warranty</div>
  </div>
  <div class="front-usa">
    <svg width="40" height="46" viewBox="0 0 40 46" aria-hidden="true">
      <path d="M20 2 L37 8 V22 C37 33 29 40 20 44 C11 40 3 33 3 22 V8 Z" fill="#fff"/>
      <g stroke="var(--gold)" stroke-width="3"><path d="M14 18v18M20 18v20M26 18v18"/></g>
    </svg>
    <span>Made in USA</span>
  </div>
</section>

<section class="card card--back">
  <div class="back-header" role="img" aria-label="Faded photo of a shuttered interior, tinted gold"></div>
  <div class="back-brand">Louver Loft</div>
  <div class="back-tagline">Houston’s Source for Plantation Shutters</div>
  <div class="back-divider"></div>
  <div class="back-call">
    <svg width="42" height="42" viewBox="0 0 42 42" aria-hidden="true">
      <path d="M10 4c2 0 4 6 4 8s-3 3-3 4c1 5 6 10 11 11 1 0 2-3 4-3s8 2 8 4-3 7-7 7C16 35 5 24 5 11c0-4 3-7 5-7z" fill="#fff"/>
      <g fill="none" stroke="#fff" stroke-width="2.5"><path d="M24 10a8 8 0 0 1 8 8M24 4a14 14 0 0 1 14 14"/></g>
    </svg>
    <div class="back-call__text">
      <div class="back-call__label">Call us today!</div>
      <div class="back-call__number">(281) 555-0187</div>
    </div>
  </div>
  <div class="back-header-line"></div>

  <div class="back-services">Custom Interior and<br>Exterior Shutters manufactured</div>
  <div class="back-address">
    <div class="back-address__name">Louver Loft</div>
    <div>8217 Calloway Ln.</div>
    <div>Houston, Texas 77099</div>
  </div>

  <div class="back-person">
    <div class="back-person__name">Name Here</div>
    <div class="back-person__title">TITLE</div>
  </div>
  <ul class="back-contacts">
    <li>(281) 555-0143
      <svg width="14" height="22" viewBox="0 0 14 22" aria-hidden="true"><rect x="1.5" y="1.5" width="11" height="19" rx="2" fill="none" stroke="var(--gold)" stroke-width="2"/><circle cx="7" cy="17" r="1.3" fill="var(--gold)"/></svg>
    </li>
    <li>louverloft@examplemail.test
      <svg width="20" height="14" viewBox="0 0 20 14" aria-hidden="true"><rect width="20" height="14" fill="var(--gold)"/><path d="M0 0l10 8 10-8" fill="none" stroke="#fff" stroke-width="1.5"/></svg>
    </li>
  </ul>

  <div class="back-footer"></div>
  <div class="back-web">www.LouverLoftHouston.test</div>
</section>

</body>
</html>
```